Bifold brochure design for leadership academy

Please see below. This is a bifold brochure for a leadership academy. (www.vesk.institute). Look and feel must be colours, shapes, abstract designs, graphics, pictures. Make this professional, yet casual and bold.

Feel free to design just the front and back cover, then I'll give feedback on whether or not you're in the right direction.

COVER
- Title: “The Brightwater Year Journey”
- “Northmere Pathways Institute” logo somewhere
- Subtitles (with images, icons, and/or shapes): “Self-discovery” “Skills development” “Real-world Impact”

PAGE 2 (Inside Fold)
- Title: "The Program"
- Section 2a: Section title: "How it works”
- Image: See website, image under "four phases of the program". Please adapt and make it look better
- Text: VPI is a structured, 8-month ‘gap year’ program for 18-25 year olds who want more than just a year off – they want a year ahead. Our aim is to develop high-potential young leaders with strong values, clear purpose, high-impact skills, and a track record of real-world accomplishments that are second-to-none. We do this through four-phases.
- Section 2b: Section title: “Dates & Timing”
- Image: See image on website under 'dates and timing'. Make sure both dates show up on the brochure (September and January program).
- Text: There are two programs per year: one that starts in September, the other in January. The first four months of the program are based in Toronto at the VPI headquarters. The curriculum we work through is highly engaging and personalized, focusing directly on students’ goals. After that, students are out in the world, achieving the remaining components of the program (e.g. internship, volunteer abroad).

PAGE 3 (Outside Fold)
- Page Title: "The Students"
- Section 3a: Section title: “Who’s it for”
- Subtitle1: “High school graduates”
 Image/icon of a high school grad
 Text1: 90% of high school grads aren't sure why they’re going to university or what they want to study.
 Text2: VPI helps students discover what they truly want to do in life, and make enormous progress towards these goals.

- Subtitle2: “Post-secondary students”
 Image/icon of a university / college student
 Text1: 28% of students switch or drop out of their program because it wasn’t for them or they didn’t like it.
 Text2: Don't keep moving around or risk switching careers down the road – find out what sparks your passion with VPI.

- Subtitle3: “Post-secondary graduates”
 Image/icon of a university/ college grad
 Text1: 50% of graduates are unemployed or underemployed, 60% are in debt.
 Text2: VPI will help you get your dream job – our students won’t settle for anything less.

- Section 3b: Section title: “How to apply”
 Text1: We select high-potential young leaders with a desire to improve themselves and impact the world.
 Text2: We won’t ask you for your grades – we care more about your values and potential.
 Text3: Visit www.vesk.institute to apply now

BACK COVER
- Page Title: “Get in Touch”
- Website: www.vesk.institute
- Facebook page: facebook.com/vesk.institute
- Twitter handle: @vesk_institute
- Email: marta@vesk.institute

Target Market(s)

18-25 year olds, parents, teachers

Industry/Entity Type

Leadership

Requirements
Must have
• Beautiful design - sleek and bold, yet colourful and casual. Keep the colours similar to our website (www.vesk.institute). See examples of other brochures.
• http://img.plorvex.net/jpg/00/11/22/33/240_F_11223344_aBcDeFgHiJkLmNoPqRsTuVwXyZ123456.jpg
• http://quandrelhub.com/wp-content/uploads/2014/11/Real-Estate-Bi-fold-Brochure.jpg
• http://www.trovanic.com/media/k2/galleries/5/001-bi-fold-brochure-psd-mock-up-template.jpg
• http://img.plorvex.net/jpg/00/44/55/66/240_F_44556677_zYxWvUtSrQpOnMlKjIhGfEdCbA987654.jpg

```html
<!DOCTYPE html>
<html lang="en">
<head>
<meta charset="utf-8">
<title>Northmere Pathways Institute – Bifold Brochure</title>
<link rel="stylesheet" href="https://fonts.googleapis.com/css2?family=Bree+Serif&family=Open+Sans:wght@400;600;700&family=Tinos:wght@400;700&display=swap">
<style>
:root{
  --stage:#e6e6e6;
  --cream:#eeeac6;
  --cream-deep:#e2dcb2;
  --navy:#2b4563;
  --maroon:#6b1f2b;
  --red:#b3202c;
  --red-box:#b8232f;
  --tan:#d6c39c;
  --blue:#1f5f93;
  --sky:#2a9fd8;
  --teal:#3d8a7a;
  --ink:#1c1c1c;
  --grey-band:#dcdcdc;
  --white:#ffffff;
}
*{box-sizing:border-box;margin:0;padding:0}
html,body{width:1200px;height:900px;overflow:hidden}
body{background:radial-gradient(ellipse at 50% 35%,#fafafa 0%,var(--stage) 75%);font-family:'Tinos',serif;color:var(--ink);position:relative}

/* ---------- Cover ---------- */
.cover{position:absolute;left:120px;top:185px;width:310px;height:540px;overflow:hidden;background:var(--cream);box-shadow:0 10px 28px rgba(0,0,0,.18)}
.cover-shapes{position:absolute;inset:0}
.cover-portrait{position:absolute;left:10px;top:118px;width:86px;height:86px;border-radius:50%;border:3px solid #e9e9e9;background:radial-gradient(circle at 50% 40%,#c9a58c,#5d4a44)}
.brand{position:absolute;right:22px;top:38px;width:130px;display:flex;align-items:flex-start;gap:6px}
.brand-mark{width:12px;height:12px;background:var(--red);flex:none;margin-top:2px}
.brand-name{font-family:'Open Sans',sans-serif;font-weight:700;font-size:13px;line-height:1.15;letter-spacing:1.5px;text-transform:uppercase;color:var(--maroon)}
.cover-title{position:absolute;left:24px;top:248px;color:var(--white);font-family:'Open Sans',sans-serif;display:flex;align-items:flex-end;gap:4px}
.cover-title .lead{font-size:13px;line-height:1.25;text-align:right;color:#f2f2f2}
.cover-title .main{font-size:44px;line-height:1;font-weight:400;color:#e8e4d8}
.pillars{position:absolute;left:122px;top:410px;list-style:none}
.pillar{display:flex;align-items:center;gap:8px;margin-bottom:12px;font-family:'Open Sans',sans-serif;font-size:12px;color:var(--maroon)}
.pillar svg{flex:none}

/* ---------- Inside spread ---------- */
.spread{position:absolute;left:565px;top:200px;width:600px;height:510px;display:flex;box-shadow:0 12px 30px rgba(0,0,0,.2)}
.page{position:relative;width:300px;height:100%;background:linear-gradient(160deg,var(--cream) 0%,var(--cream-deep) 100%);overflow:hidden}
.page + .page{border-left:1px solid #cfc8a0}

.page-title{position:absolute;top:30px;font-family:'Bree Serif',serif;font-size:17px;padding:3px 10px;transform:rotate(-3deg)}
.page-title.program{left:26px;color:var(--red);background:var(--cream);border:2px solid var(--tan);box-shadow:2px 2px 0 #b9a77d}
.page-title.students{left:20px;color:var(--white);background:var(--teal);box-shadow:2px 2px 0 #2b6458}
.lead-line{position:absolute;left:0;height:1px}
.lead-line::after{content:"";position:absolute;right:-3px;top:-3px;width:7px;height:7px;border-radius:50%;background:inherit}
.lead-line.blue{background:var(--sky)}
.lead-line.red{background:var(--red)}

.section-label{position:absolute;font-family:'Tinos',serif;font-weight:700;font-size:9px;padding:2px 5px;border:1px dashed var(--red);background:var(--cream)}

.magnifier{position:absolute;left:168px;top:8px;width:112px;height:74px;border-radius:6px;background:linear-gradient(90deg,var(--red) 0 55%,var(--blue) 55%);opacity:.85}

.body-copy{position:absolute;left:34px;width:240px;font-size:6.6px;line-height:1.45;text-align:justify}

.phases{position:absolute;left:20px;top:206px;width:260px;display:flex;justify-content:space-between}
.phase{width:56px;text-align:center;font-size:5.5px;font-weight:700}
.phase .ring{width:44px;height:44px;margin:3px auto 0;border-radius:50%;border:1.5px dotted var(--red);display:flex;align-items:center;justify-content:center}
.phase .art{width:28px;height:28px;border-radius:4px;background:linear-gradient(#d6d3c4,#9a968a)}
.phase .tag{display:inline-block;margin-top:2px;background:var(--red);color:var(--white);font-size:4.5px;padding:1px 4px}

.calendars{position:absolute;left:126px;top:300px;display:flex;gap:18px}
.calendar{width:54px;background:#f4f4f4;box-shadow:0 1px 2px rgba(0,0,0,.25)}
.calendar-head{color:var(--white);font-family:'Open Sans',sans-serif;font-size:5px;text-align:center;padding:2px 0}
.calendar.sep .calendar-head{background:var(--red)}
.calendar.jan .calendar-head{background:var(--blue)}
.calendar-grid{padding:3px;display:grid;grid-template-columns:repeat(7,1fr);gap:2px}
.calendar-grid span{height:3px;background:#9a9a9a}
.timing-notes{position:absolute;left:112px;top:365px;width:170px;display:flex;justify-content:space-between;font-family:'Open Sans',sans-serif;font-weight:700;font-size:5px}
.timing-notes .full{color:var(--red)}
.timing-notes .monthly{color:var(--sky)}

/* Students page */
.audience-head{position:absolute;left:14px;top:108px;width:272px;height:18px;background:var(--grey-band);display:flex}
.audience-head span{flex:1;font-size:6px;font-weight:700;color:var(--blue);display:flex;align-items:center;justify-content:center;border-left:1px dashed var(--red)}
.audience-head span:first-child{border-left:0}
.audience-icons{position:absolute;left:14px;top:134px;width:272px;display:flex}
.audience-icons div{flex:1;display:flex;justify-content:center}
.audience-icons .art{width:30px;height:40px;border-radius:15px 15px 4px 4px;background:var(--red-box)}
.audience-box{position:absolute;left:14px;top:186px;width:272px;height:132px;background:var(--red-box);display:flex}
.audience-col{flex:1;padding:8px 6px;color:var(--white);font-size:6px;line-height:1.4;text-align:center;border-left:1px dashed rgba(255,255,255,.5)}
.audience-col:first-child{border-left:0}
.audience-col p + p{margin-top:10px}

.apply-steps{position:absolute;left:18px;top:372px;width:262px;list-style:none}
.apply-step{display:flex;height:26px;margin-bottom:7px;background:var(--blue);color:var(--white);font-size:6.5px;align-items:center}
.apply-step .num{width:22px;height:100%;display:flex;align-items:center;justify-content:center;border-right:1px solid rgba(255,255,255,.6);font-size:8px}
.apply-step .text{padding:0 8px}
</style>
</head>
<body>

<!-- Front cover -->
<section class="cover" aria-label="Front cover">
  <svg class="cover-shapes" viewBox="0 0 310 540" width="310" height="540" aria-hidden="true">
    <defs>
      <linearGradient id="navyPhoto" x1="0" y1="0" x2="1" y2="1">
        <stop offset="0" stop-color="#3a5575"/><stop offset="1" stop-color="#1e3046"/>
      </linearGradient>
      <linearGradient id="maroonPhoto" x1="0" y1="0" x2="1" y2="1">
        <stop offset="0" stop-color="#7d2432"/><stop offset="1" stop-color="#4f1520"/>
      </linearGradient>
      <linearGradient id="tanBand" x1="0" y1="0" x2="1" y2="1">
        <stop offset="0" stop-color="#dfcda6"/><stop offset="1" stop-color="#c7b085"/>
      </linearGradient>
    </defs>
    <polygon points="0,0 130,0 220,150 0,330" fill="url(#navyPhoto)"/>
    <polygon points="220,150 310,110 310,300 0,520 0,330" fill="url(#maroonPhoto)"/>
    <polygon points="310,300 310,540 0,540 0,520" fill="url(#tanBand)"/>
  </svg>
  <div class="cover-photo" role="img" aria-label="Photo of a young student in glasses, tinted navy and maroon" style="position:absolute;inset:0"></div>
  <div class="cover-portrait" role="img" aria-label="Circular portrait photo of a student"></div>

  <div class="brand">
    <span class="brand-mark"></span>
    <span class="brand-name">Northmere Pathways Institute</span>
  </div>

  <h1 class="cover-title">
    <span class="lead">The Brightwater<br>Year</span>
    <span class="main">Journey</span>
  </h1>

  <ul class="pillars">
    <li class="pillar"><svg width="20" height="20" viewBox="0 0 20 20"><polygon points="10,1 18,5.5 18,14.5 10,19 2,14.5 2,5.5" fill="#c9463c"/></svg>Self-discovery</li>
    <li class="pillar"><svg width="20" height="20" viewBox="0 0 20 20"><polygon points="10,1 18,5.5 18,14.5 10,19 2,14.5 2,5.5" fill="#6a5ba8"/></svg>Skills Development</li>
    <li class="pillar"><svg width="20" height="20" viewBox="0 0 20 20"><polygon points="10,1 18,5.5 18,14.5 10,19 2,14.5 2,5.5" fill="#c9463c"/></svg>Real-world Impact</li>
  </ul>
</section>

<!-- Inside spread -->
<section class="spread" aria-label="Inside spread">
  <article class="page">
    <span class="lead-line blue" style="top:44px;width:26px"></span>
    <h2 class="page-title program">The Program</h2>
    <div class="magnifier" role="img" aria-label="Magnifying glass over coloured list bars"></div>

    <span class="lead-line red" style="top:86px;width:28px"></span>
    <h3 class="section-label" style="left:30px;top:79px">How it works ?</h3>
    <p class="body-copy" style="top:110px">VPI is a structured, 8-month ‘gap year’ program for 18-25 year olds who want more than just a year off – they want a year ahead. Our aim is to develop high-potential young leaders with strong values, clear purpose, high-impact skills, and a track record of real-world accomplishments that are second-to-none. We do this through four-phases.</p>

    <div class="phases">
      <div class="phase">Discover<div class="ring"><div class="art" role="img" aria-label="Student figure"></div></div><span class="tag">START</span></div>
      <div class="phase">Design<div class="ring"><div class="art" role="img" aria-label="Planning document"></div></div></div>
      <div class="phase">Build<div class="ring"><div class="art" role="img" aria-label="Presentation board"></div></div></div>
      <div class="phase">Achieve<div class="ring"><div class="art" role="img" aria-label="Celebrating student"></div></div><span class="tag">FINISH</span></div>
    </div>

    <span class="lead-line red" style="top:297px;width:28px"></span>
    <h3 class="section-label" style="left:30px;top:290px">Dates &amp; Timing</h3>

    <div class="calendars">
      <div class="calendar sep"><div class="calendar-head">SEPTEMBER</div>
        <div class="calendar-grid"><span></span><span></span><span></span><span></span><span></span><span></span><span></span><span></span><span></span><span></span><span></span><span></span><span></span><span></span><span></span><span></span><span></span><span></span><span></span><span></span><span></span><span></span><span></span><span></span><span></span><span></span><span></span><span></span></div></div>
      <div class="calendar jan"><div class="calendar-head">JANUARY</div>
        <div class="calendar-grid"><span></span><span></span><span></span><span></span><span></span><span></span><span></span><span></span><span></span><span></span><span></span><span></span><span></span><span></span><span></span><span></span><span></span><span></span><span></span><span></span><span></span><span></span><span></span><span></span><span></span><span></span><span></span><span></span></div></div>
    </div>
    <div class="timing-notes"><span class="full">FULL TIME IN CLASSROOM</span><span class="monthly">MONTHLY CHECKPOINTS</span></div>

    <p class="body-copy" style="top:400px">There are two programs per year: one that starts in September, the other in January. The first four months of the program are based in Toronto at the VPI headquarters. The curriculum we work through is highly engaging and personalized, focusing directly on students’ goals. After that, students are out in the world, achieving the remaining components of the program (e.g. internship, volunteer abroad).</p>
  </article>

  <article class="page">
    <h2 class="page-title students">The Students</h2>

    <span class="lead-line red" style="top:86px;width:24px"></span>
    <h3 class="section-label" style="left:26px;top:79px">Who’s it for ?</h3>

    <div class="audience-head"><span>High school graduates</span><span>Post-secondary students</span><span>Post-secondary graduates</span></div>
    <div class="audience-icons">
      <div><div class="art" role="img" aria-label="High school graduate icon"></div></div>
      <div><div class="art" role="img" aria-label="College student icon"></div></div>
      <div><div class="art" role="img" aria-label="University graduate icon"></div></div>
    </div>
    <div class="audience-box">
      <div class="audience-col"><p>90% of high school grads aren't sure why they’re going to university or what they want to study.</p><p>VPI helps students discover what they truly want to do in life, and make enormous progress towards these goals.</p></div>
      <div class="audience-col"><p>28% of students switch or drop out of their program because it wasn’t for them or they didn’t like it.</p><p>Don't keep moving around or risk switching careers down the road – find out what sparks your passion with VPI.</p></div>
      <div class="audience-col"><p>50% of graduates are unemployed or underemployed, 60% are in debt.</p><p>VPI will help you get your dream job – our students won’t settle for anything less.</p></div>
    </div>

    <span class="lead-line red" style="top:350px;width:24px"></span>
    <h3 class="section-label" style="left:26px;top:343px">How to Apply ?</h3>
    <ol class="apply-steps">
      <li class="apply-step"><span class="num">1</span><span class="text">We select high-potential young leaders with a desire to improve themselves and impact the world.</span></li>
      <li class="apply-step"><span class="num">2</span><span class="text">We won’t ask you for your grades – we care more about your values and potential.</span></li>
      <li class="apply-step"><span class="num">3</span><span class="text">Visit www.vesk.institute to apply now</span></li>
    </ol>
  </article>
</section>

</body>
</html>
```